business card design - photography

I am a fine art photographer. I would like to approach galleries to exhibit my work and need a business card.

The card should convey creativity and simplicity.
I would like a double sided card.

Some options:
1. An all white card with raised or embossed text or design to create a tactile finish.
2. a white and dark grey design would also work well.
3. Would be great to use my name as part of the design but not essential.
4. My name and title on the front, other details on the back of card.

The final design should be simple, minimal, elegant and innovative.
Being minimal, it will be more about texture, text size and placement.

examples of designs I would prefer provided here:
http://layoutmuse.net/ideas/40-plain-and-graceful-calling-card-layouts

I'm also open to other designs that may be unusual and unique.

Love this:
http://www.snapvault.com/pics/morningverses/583017264
Updates

I have uploaded a psd file after playing around in photoshop with various fonts.  I like the font (which I downloaded from typeshelf.net called Arual) but the design probably needs some refining.  I hope this helps.  If you'd like me to change the format of the file, please let me know.

Marta

Target Market(s)

Art Gallery owners/administrators and customers.

Industry/Entity Type

Business

Requirements
Must have
• A unique look.

Matte, silky finish or heavy textured stock. Double-sided card.

Front:
my name
photography by

Back:
phone no
email
web address
Nice to have
• Letterpress
embrossed
Clean fonts
Should not have
• Do not use illustrations of cameras or lenses.
No frames around the card edge.

```html
<!DOCTYPE html>
<html lang="en">
<head>
<meta charset="utf-8">
<title>Marta Halden Photographer – Business Card</title>
<link rel="stylesheet" href="https://fonts.googleapis.com/css2?family=Mulish:wght@200;300;400;800&display=swap">
<style>
  :root {
    --backdrop: #d4d4d4;
    --card-red-deep: #7f1114;
    --card-red: #a3191c;
    --card-red-light: #b21e21;
    --card-white: #ffffff;
    --ink-white: #ffffff;
    --ink-red: #a3191c;
    --ink-grey: #4a4a4a;
  }
  html, body {
    margin: 0;
    padding: 0;
    width: 1200px;
    height: 900px;
    overflow: hidden;
    background: var(--backdrop);
    font-family: "Mulish", sans-serif;
  }
  .canvas {
    position: relative;
    width: 1200px;
    height: 900px;
    background: radial-gradient(ellipse at 50% 40%, #e2e2e2 0%, var(--backdrop) 70%);
  }
  .card {
    position: absolute;
    top: 300px;
    width: 520px;
    height: 300px;
    box-shadow: 0 2px 6px rgba(0, 0, 0, 0.18);
  }
  .card--front {
    left: 68px;
    background: linear-gradient(135deg, var(--card-red-deep) 0%, var(--card-red) 45%, var(--card-red-light) 100%);
  }
  .card--back {
    left: 612px;
    background: var(--card-white);
  }
  .name-line {
    position: absolute;
    right: 4px;
    top: 178px;
    margin: 0;
    white-space: nowrap;
    font-size: 40px;
    line-height: 1;
    color: var(--ink-white);
    letter-spacing: 0.2px;
  }
  .name-line__name {
    font-weight: 800;
  }
  .name-line__title,
  .title-tail {
    font-weight: 200;
  }
  .title-tail {
    position: absolute;
    left: 2px;
    top: 178px;
    margin: 0;
    font-size: 40px;
    line-height: 1;
    color: var(--ink-red);
  }
  .contact {
    position: absolute;
    right: 26px;
    top: 96px;
    margin: 0;
    text-align: right;
    font-size: 15px;
    line-height: 1.35;
    font-weight: 400;
    color: var(--ink-grey);
    font-style: normal;
  }
</style>
</head>
<body>
  <main class="canvas">
    <section class="card card--front" aria-label="Card front">
      <h1 class="name-line">
        <span class="name-line__name">Marta Halden</span>
        <span class="name-line__title">Photo</span>
      </h1>
    </section>
    <section class="card card--back" aria-label="Card back">
      <p class="title-tail">grapher</p>
      <address class="contact">
        0400 218 947<br>
        mhalden@mailbox.net<br>
        www.martahalden.net
      </address>
    </section>
  </main>
</body>
</html>
```